IT Services

We come to you
Only $49/hr
No contract, no monthly fee
Software engineer on staff
remote assistance or visit in your office

On the back of the card I want to list services.

- Server setup
- Network troubleshooting
- Printer setup
- Secure backup setup
- Software installation
- Wireless network setup
- Wired network setup
- Disaster recovery
- Website management
- Any other technology related support
- Email setup
- HIPAA compliance review and setup
Updates

the URL is: BYTEHARBOR.ZONE please use it on the card

On the card we need to mention "Connect remotely to address your IT issues" if there is enough room as well as "we go to you"

Industry/Entity Type

Printer

Contact Information for Business Card

I want a busoiness card to offer my services to doctor offices, it can be dentists, Otamatry, and other professions. I provide the following service. My plan is to go to their office and drop off my card. I don't want them to forget about it that is why I am paying for the design. I like hand writing design formats.

```html
<!DOCTYPE html>
<html lang="en">
<head>
<meta charset="utf-8">
<title>IT Services Business Card</title>
<link rel="stylesheet" href="https://fonts.googleapis.com/css2?family=Patrick+Hand&display=swap">
<style>
  :root {
    --page-bg: #74665a;
    --back-card: #fde6b2;
    --front-card-top: #fde6db;
    --front-card-bottom: #fbd9cf;
    --ink: #111111;
    --band: #050505;
    --band-text: #ffffff;
    --art-warm: rgba(235, 170, 90, 0.35);
    --art-pink: rgba(230, 120, 140, 0.30);
  }
  * { margin: 0; padding: 0; box-sizing: border-box; }
  html, body {
    width: 1200px;
    height: 1200px;
    overflow: hidden;
    background: var(--page-bg);
  }
  body {
    position: relative;
    font-family: "Patrick Hand", cursive;
    color: var(--ink);
  }
  .card {
    position: absolute;
    top: 172px;
    width: 516px;
    height: 884px;
    overflow: hidden;
    box-shadow: 0 6px 18px rgba(0, 0, 0, 0.35);
  }
  /* Services side */
  .card-services {
    left: 58px;
    background: var(--back-card);
  }
  .services-art {
    position: absolute;
    left: 20px;
    top: 330px;
    width: 480px;
    height: 330px;
    background: radial-gradient(ellipse at 45% 50%, var(--art-warm) 0%, rgba(253, 230, 178, 0) 70%);
  }
  .service-list {
    position: absolute;
    left: 30px;
    top: 38px;
    list-style: none;
  }
  .service-item {
    display: flex;
    align-items: center;
    height: 61px;
    font-size: 25px;
    line-height: 1;
  }
  .folder-icon {
    width: 28px;
    height: 22px;
    margin-right: 17px;
    flex-shrink: 0;
  }
  .phone-band {
    position: absolute;
    left: 0;
    bottom: 0;
    width: 100%;
    height: 114px;
    background: var(--band);
    color: var(--band-text);
    display: flex;
    align-items: center;
    justify-content: center;
    gap: 24px;
    font-size: 50px;
    letter-spacing: 1px;
  }
  .phone-band::before {
    content: "";
    position: absolute;
    left: 170px;
    top: -10px;
    width: 172px;
    height: 20px;
    background: var(--band);
    border-radius: 12px 12px 0 0;
  }
  .phone-icon { width: 42px; height: 46px; }

  /* Offer side */
  .card-offer {
    left: 626px;
    background: linear-gradient(180deg, var(--front-card-top) 0%, var(--front-card-bottom) 100%);
    text-align: center;
  }
  .offer-art {
    position: absolute;
    left: 0;
    top: 60px;
    width: 100%;
    height: 760px;
    background:
      radial-gradient(ellipse at 40% 45%, var(--art-pink) 0%, rgba(251, 217, 207, 0) 55%),
      radial-gradient(ellipse at 75% 75%, rgba(250, 235, 200, 0.5) 0%, rgba(251, 217, 207, 0) 50%);
  }
  .offer-text, .contact-block {
    position: absolute;
    left: 0;
    width: 100%;
  }
  .offer-text { top: 60px; }
  .headline { font-size: 58px; line-height: 70px; }
  .price { font-size: 42px; line-height: 58px; }
  .terms { font-size: 34px; line-height: 56px; }
  .detail { font-size: 27px; line-height: 40px; }
  .contact-block { top: 600px; }
  .contact-name { font-size: 40px; line-height: 60px; }
  .contact-url { font-size: 58px; line-height: 74px; }
  .contact-phone { font-size: 42px; line-height: 70px; }
</style>
</head>
<body>
  <svg width="0" height="0" style="position:absolute">
    <defs>
      <symbol id="folder" viewBox="0 0 28 22">
        <path d="M1.5 3.5 h8 l2 2.5 h15 v14.5 h-25 z" fill="none" stroke="#111" stroke-width="1.6" stroke-linejoin="round"/>
        <path d="M1.5 8.5 h25" stroke="#111" stroke-width="1.4"/>
        <path d="M4 11 l3 7 M9 11 l3 7 M14 11 l3 7 M19 11 l3 7" stroke="#111" stroke-width="1"/>
      </symbol>
    </defs>
  </svg>

  <section class="card card-services">
    <div class="services-art" role="img" aria-label="Faint sketch of a computer and cables behind the service list"></div>
    <ul class="service-list">
      <li class="service-item"><svg class="folder-icon"><use href="#folder"/></svg>Server setup</li>
      <li class="service-item"><svg class="folder-icon"><use href="#folder"/></svg>Network troubleshooting</li>
      <li class="service-item"><svg class="folder-icon"><use href="#folder"/></svg>Printer setup</li>
      <li class="service-item"><svg class="folder-icon"><use href="#folder"/></svg>Secure backup setup</li>
      <li class="service-item"><svg class="folder-icon"><use href="#folder"/></svg>Software installation</li>
      <li class="service-item"><svg class="folder-icon"><use href="#folder"/></svg>Wireless network setup</li>
      <li class="service-item"><svg class="folder-icon"><use href="#folder"/></svg>Wired network setup</li>
      <li class="service-item"><svg class="folder-icon"><use href="#folder"/></svg>Disaster recovery</li>
      <li class="service-item"><svg class="folder-icon"><use href="#folder"/></svg>Website management</li>
      <li class="service-item"><svg class="folder-icon"><use href="#folder"/></svg>Any other technology related support</li>
      <li class="service-item"><svg class="folder-icon"><use href="#folder"/></svg>Email setup</li>
      <li class="service-item"><svg class="folder-icon"><use href="#folder"/></svg>HIPAA compliance review and setup</li>
    </ul>
    <div class="phone-band">
      <svg class="phone-icon" viewBox="0 0 42 46" aria-hidden="true">
        <path d="M9 3 l7 9 l-5 5 c2 7 7 13 14 16 l5 -5 l9 7 l-5 7 c-14 0 -30 -17 -31 -31 z" fill="none" stroke="#fff" stroke-width="2.2" stroke-linejoin="round"/>
      </svg>
      <span>1-800-555-0147</span>
    </div>
  </section>

  <section class="card card-offer">
    <div class="offer-art" role="img" aria-label="Soft pink circuit and fiber-optic light decoration"></div>
    <div class="offer-text">
      <p class="headline">We come to you</p>
      <p class="price">Only $49/hr</p>
      <p class="terms">No contract, no monthly fee</p>
      <p class="detail">Software engineer on staff</p>
      <p class="detail">remote assistance or visit in your office</p>
    </div>
    <div class="contact-block">
      <p class="contact-name">Dara Venn</p>
      <p class="contact-url">byteharbor.zone</p>
      <p class="contact-phone">1-800-555-0147</p>
    </div>
  </section>
</body>
</html>
```